Brochure Design Project for Building Designer

I need a modern and edgy brochure to introduce my new business TORV Design, Commercial and Residential Building Designers.

We specialise in Building Design, Project Management and Design Consultation.

I would like the brochure to be anywhere between 2-4 pages, depending of amount of suitable content available.
Colours to be black and white with splashes of
bright colours (mostly incorporated in photos).

Main Content of brochure to be broken up into 3 (maybe 4) sections to include:

About Us
Services
Projects

Logo Text (DESIGN etc) can be changed to white if suits better with black background.

Would be nice to include sketches to give it that architectural feel.

Samples and wording will be uploaded shortly
Updates

I HAVE PROVIDED A COMPLETE UPDATE OF PROJECT REQUIREMENTS INCLUDING ALL NEW UPLOADED FILES.

PLEASE REFER TO THE BROCHURE LAYOUT PDF UPLOADEDĀ FOR FULL INFORMATION ON PROJECT INCLUDING BROCHURE LAYOUT.

IF YOU HAVE ANY QUESTIONS OR REQUIRE ANY FURTHER INFORMATION, PLEASE LET ME KNOW

I HAVE ADDED FURTHER DEVELOPED PDF DOCUMENTS OF BROCHURE.

IF YOU HAVE TROUBLE OPENING THESE DOCS IN ADOBE ILLUSTRATOR THRU ADOBE BRIDGE PLEASE LET ME KNOW & I WILL UPLOAD AI FILES.

CAN YOU PLEASE FINE TUNE GRAPHICS AND WORK ON BACKGROUND

Target Market(s)

Builders, Property Developers, Architects, Consultants, Professionals

Industry/Entity Type

Business

Requirements
Must have
• Very Professional Look
Black and White
Simple and easy to read layout
Either A4 (if only 2 pages) or
A3 double sided with centre fold (if 4 pages)
Touch up of photos (if possible) to make them stand out of the page.
Samples of recent projects with photos
Should not have
• Any comics or similar

```html
<!DOCTYPE html>
<html lang="en">
<head>
<meta charset="utf-8">
<title>TORV Design – Brochure Inner Pages</title>
<link rel="stylesheet" href="https://fonts.googleapis.com/css2?family=Dosis:wght@300;400;600;700&family=PT+Sans+Narrow:wght@400;700&display=swap">
<style>
  :root {
    --backdrop: #ecebe8;
    --paper: #ffffff;
    --ink-grey: #8d8883;
    --ink-soft: #9a9691;
    --ink-strong: #5f5b57;
    --accent-pink: #e8659a;
    --pool-teal: #3ec4c8;
    --pool-deep: #2aa9ae;
    --band-grey: #dcdcdc;
  }
  * { box-sizing: border-box; margin: 0; padding: 0; }
  html, body { width: 1200px; height: 900px; overflow: hidden; }
  body { background: var(--backdrop); position: relative; font-family: "Dosis", sans-serif; }

  .spread {
    position: absolute; left: 111px; top: 104px;
    width: 977px; height: 691px;
    transform: scale(1.15); transform-origin: center center;
    background: var(--paper);
    box-shadow: 0 2px 6px rgba(0,0,0,0.15);
  }
  .page { position: absolute; top: 0; height: 691px; overflow: hidden; background: var(--paper); }
  .page--left { left: 0; width: 489px; }
  .page--right { left: 489px; width: 488px; border-left: 1px solid #e4e4e4; }

  .photo { position: absolute; }

  /* left page photography */
  .photo--exterior { left: 0; top: 0; width: 210px; height: 221px;
    background:
      radial-gradient(ellipse 60% 45% at 60% 45%, rgba(240,240,240,0.95) 0%, rgba(200,200,200,0.6) 45%, rgba(0,0,0,0) 75%),
      linear-gradient(180deg, #3a3a3a 0%, #2a2a2a 30%, #6f6f6f 70%, #4d4d4d 100%); }
  .photo--terrace { left: 0; top: 233px; width: 210px; height: 130px;
    background:
      radial-gradient(ellipse 70% 60% at 30% 40%, rgba(225,225,225,0.9) 0%, rgba(0,0,0,0) 70%),
      linear-gradient(180deg, #5a5a5a 0%, #8c8c8c 55%, #3f3f3f 100%); }
  .photo--interior { left: 222px; top: 0; width: 267px; height: 363px;
    background:
      radial-gradient(ellipse 55% 35% at 30% 30%, rgba(255,255,255,0.9) 0%, rgba(255,255,255,0) 70%),
      linear-gradient(160deg, rgba(0,0,0,0) 50%, rgba(20,20,20,0.75) 72%, rgba(40,40,40,0.5) 100%),
      linear-gradient(180deg, #ededed 0%, #d4d4d4 35%, #9e9e9e 58%, #5a5a5a 75%, #cfcfcf 100%); }
  .band { position: absolute; left: 0; top: 363px; width: 489px; height: 64px;
    background: linear-gradient(180deg, var(--band-grey), #f6f6f6); }

  .about { position: absolute; left: 39px; top: 146px; width: 250px; height: 250px; }
  .about__circle { position: absolute; inset: 0; border-radius: 50%;
    background: var(--accent-pink); border: 9px solid var(--paper);
    box-shadow: 0 1px 4px rgba(0,0,0,0.2); }
  .about__title { position: absolute; left: 60px; top: 64px; color: #fff; white-space: nowrap;
    font-family: "PT Sans Narrow", sans-serif; font-weight: 700; font-size: 32px; letter-spacing: 0.3px; }
  .about__text { position: absolute; left: 60px; top: 130px; width: 162px; color: #fff;
    font-family: "PT Sans Narrow", sans-serif; font-size: 12px; line-height: 15.5px; }
  .about__line { display: block; white-space: nowrap; text-align: justify; text-align-last: justify; }
  .about__line--last { text-align-last: left; }
  .about__text strong { font-weight: 700; }

  .experience__title { position: absolute; left: 36px; top: 456px; color: var(--ink-grey);
    font-weight: 600; font-size: 34px; line-height: 43px; letter-spacing: 0.3px; white-space: nowrap; }
  .experience__list { position: absolute; left: 235px; top: 459px; list-style: none;
    color: var(--ink-soft); font-size: 11px; font-weight: 400; white-space: nowrap; }
  .experience__list li { height: 23px; line-height: 14px; }
  .experience__list strong { color: var(--ink-strong); font-weight: 700; }

  .brand { position: absolute; left: 32px; top: 632px; color: var(--ink-grey);
    font-weight: 700; font-size: 17px; letter-spacing: 1px; white-space: nowrap; }

  /* right page */
  .photo--bedroom { left: 0; top: 0; width: 193px; height: 147px;
    background:
      radial-gradient(ellipse 45% 35% at 55% 40%, rgba(255,255,255,1) 0%, rgba(255,255,255,0) 80%),
      linear-gradient(180deg, #dcdcdc 0%, #c4c4c4 45%, #5a5a5a 70%, #7a7a7a 85%, #3a3a3a 100%); }
  .ethos { position: absolute; left: 36px; top: 171px; color: var(--ink-strong); white-space: nowrap;
    font-weight: 300; font-size: 20px; line-height: 26.5px; letter-spacing: 0.6px; }
  .services__title { position: absolute; left: 234px; top: 30px; color: var(--ink-grey);
    font-weight: 600; font-size: 34px; letter-spacing: 0.3px; }
  .services__list { position: absolute; left: 234px; top: 91px; list-style: none; white-space: nowrap;
    color: var(--ink-soft); font-weight: 400; font-size: 11px; text-transform: uppercase; }
  .services__list li { height: 23.2px; line-height: 14px; }
  .photo--apartments { left: 0; top: 405px; width: 488px; height: 286px;
    background:
      linear-gradient(90deg, rgba(255,255,255,0) 0%, rgba(255,255,255,0.25) 50%, rgba(255,255,255,0) 100%),
      linear-gradient(180deg,
        #ffffff 0%, #f2f2f2 12%, #a9a9a9 22%, #8a8a8a 45%, #bdbdbd 62%,
        #4a4a4a 70%, #7c7c7c 78%, #b8b8b8 80.5%,
        var(--pool-teal) 81.5%, var(--pool-deep) 100%); }
</style>
</head>
<body>
  <div class="spread">
    <section class="page page--left">
      <div class="photo photo--exterior" role="img" aria-label="Black and white photo of a modern multi-storey house exterior at dusk"></div>
      <div class="photo photo--terrace" role="img" aria-label="Black and white photo of a house terrace detail"></div>
      <div class="photo photo--interior" role="img" aria-label="Black and white photo of an open-plan interior with staircase and dining table"></div>
      <div class="band"></div>

      <div class="about">
        <div class="about__circle"></div>
        <h2 class="about__title">ABOUT US</h2>
        <p class="about__text">
          <span class="about__line"><strong>TORV DESIGN</strong> has a diverse port-</span>
          <span class="about__line">folio of commercial + residential</span>
          <span class="about__line">work across a range of scales,</span>
          <span class="about__line about__line--last">budgets + project types.</span>
        </p>
      </div>

      <h2 class="experience__title">ARE AS OF<br>EXPERIENCE<br>INCLUDE:</h2>
      <ul class="experience__list">
        <li>– <strong>COMMERCIAL</strong> DEVELOPMENTS</li>
        <li>– <strong>MIXED-USE</strong> DEVELOPMENTS</li>
        <li>– <strong>RESIDENTIAL</strong> &amp; MULTI RESIDENTIAL</li>
        <li>– UPMARKET <strong>INDIVIDUAL</strong> HOUSES</li>
        <li>– <strong>HEALTH</strong>CARE</li>
        <li>– COMMERCIAL <strong>INDUSTRIAL</strong></li>
        <li>– CAFES/<strong>RESTAURANTS</strong></li>
        <li>– <strong>ALTERATIONS</strong> + ADDITIONS</li>
        <li>– RESIDENTIAL + <strong>COMMERCIAL</strong> INTERIOR FITOUTS</li>
      </ul>

      <div class="brand">TORV DESIGN</div>
    </section>

    <section class="page page--right">
      <div class="photo photo--bedroom" role="img" aria-label="Black and white photo of a bedroom with a made bed"></div>
      <p class="ethos">WE STRIVE TO BE<br>EFFICIENT AT ALL<br>TIMES IN EVERY<br>ASPECT OF OUR<br>SERVICE + PRIDE<br>OURSELVES ON<br>OUR ATTENTION<br>TO DETAIL.</p>

      <h2 class="services__title">SERVICES</h2>
      <ul class="services__list">
        <li>Project Planning</li>
        <li>Design Concepts</li>
        <li>Design Development / Development Approval</li>
        <li>Consultant Liaison + Management</li>
        <li>Building Certification</li>
        <li>Tender / Construction</li>
        <li>Documentation</li>
        <li>Project Management</li>
        <li>3D Modelling &amp; Renders</li>
        <li>Re-Documentation &amp; Design Consultation</li>
        <li>Drafting Services</li>
      </ul>

      <div class="photo photo--apartments" role="img" aria-label="Black and white photo of an apartment block with a turquoise swimming pool in front"></div>
    </section>
  </div>
</body>
</html>
```